Business Card for Business consulting practice

Need a design for a consultant business card. Simple and elegant.
I need the following information on the card:
Logo: (see uploaded file)
Company name: Calmora Advisory Group
Name: Dana Weltrup
Title: Managing Director - Aerospace and Defence
Phone #: 514-268-3917
e-mail: dana.weltrup@calmora-example.com
Website: www.calmora-example.com
Tagline: Proposals Management and Capture support for complex procurements

```html
<!DOCTYPE html>
<html lang="en">
<head>
<meta charset="utf-8">
<title>Calmora Advisory Group – Business Card</title>
<link href="https://fonts.googleapis.com/css2?family=Cinzel:wght@500&family=Plus+Jakarta+Sans:ital,wght@0,400;0,500;0,600;1,400;1,500;1,700&display=swap" rel="stylesheet">
<style>
  :root {
    --navy: #0e2f42;
    --accent: #2196c4;
    --white: #ffffff;
    --page: #ffffff;
    --shadow: rgba(0, 0, 0, 0.55);
  }
  * { margin: 0; padding: 0; box-sizing: border-box; }
  html, body {
    width: 1200px;
    height: 1000px;
    overflow: hidden;
    background: var(--page);
    font-family: "Plus Jakarta Sans", Arial, sans-serif;
  }
  .card {
    position: absolute;
    left: 285px;
    width: 630px;
    height: 368px;
    background: var(--navy);
    box-shadow: 14px 16px 14px var(--shadow);
    overflow: hidden;
  }
  .card--front { top: 95px; }
  .card--back { top: 536px; }

  .front__website {
    position: absolute;
    left: 22px;
    top: 105px;
    transform-origin: left top;
    transform: translateX(21px) rotate(90deg);
    color: var(--accent);
    font-size: 17px;
    letter-spacing: 0.3px;
    white-space: nowrap;
  }
  .wordmark {
    position: absolute;
    color: var(--white);
    font-family: "Cinzel", Georgia, serif;
    font-weight: 500;
    white-space: nowrap;
    text-align: center;
    letter-spacing: 1px;
  }
  .front__wordmark {
    left: 0;
    right: 0;
    top: 160px;
    font-size: 34px;
  }
  .back__wordmark {
    left: 60px;
    width: 225px;
    top: 168px;
    font-size: 16px;
  }

  .back__swoosh {
    position: absolute;
    right: 0;
    top: 0;
  }
  .back__divider {
    position: absolute;
    left: 307px;
    top: 112px;
    width: 1px;
    height: 145px;
    background: var(--white);
  }
  .contact {
    position: absolute;
    left: 331px;
    top: 108px;
    color: var(--white);
  }
  .contact__name {
    font-size: 20px;
    font-weight: 600;
    line-height: 26px;
  }
  .contact__title {
    color: var(--accent);
    font-size: 14px;
    font-style: italic;
    line-height: 17px;
  }
  .contact__phone,
  .contact__email {
    font-size: 16px;
    line-height: 21px;
  }
  .contact__phone { margin-top: 18px; }
  .contact__web {
    margin-top: 9px;
    color: var(--accent);
    font-size: 18px;
    font-weight: 700;
    font-style: italic;
  }
  .tagline {
    position: absolute;
    left: 0;
    right: 0;
    top: 306px;
    text-align: center;
    color: var(--white);
    font-size: 14px;
    font-style: italic;
    padding-right: 10px;
  }
</style>
</head>
<body>
  <section class="card card--front">
    <div class="front__website">www.calmora-example.com</div>
    <div class="wordmark front__wordmark">Calmora Advisory Group</div>
  </section>

  <section class="card card--back">
    <svg class="back__swoosh" width="140" height="150" viewBox="490 0 140 150" aria-hidden="true">
      <path d="M497,0 C512,80 565,135 630,145 L630,118 C575,110 525,70 512,0 Z" fill="var(--accent)"/>
      <path d="M512,0 C525,70 575,110 630,118 L630,106 C585,95 545,55 540,0 Z" fill="var(--white)"/>
    </svg>

    <div class="wordmark back__wordmark">Calmora Advisory Group</div>
    <div class="back__divider"></div>

    <div class="contact">
      <div class="contact__name">Dana Weltrup</div>
      <div class="contact__title">Managing Director<br>- Aerospace and Defence</div>
      <div class="contact__phone">514-268-3917</div>
      <div class="contact__email">dana.weltrup@calmora-example.com</div>
      <div class="contact__web">www.calmora-example.com</div>
    </div>

    <p class="tagline">Proposals Management and Capture support for complex procurements</p>
  </section>
</body>
</html>
```